Corporate Business Card

Very professional, Modern, Not to busy, include phone address email, website
(360) 555-0174, 61807 19th Street N, Marlow, OR 98517, marcus@kestrelbayholding.com, brelvanindustries.com

Target Market(s)

Manufacturing

Industry/Entity Type

Aero, machining, manufacturing, Off road racing

Contact Information for Business Card

Phone, address email, website

```html
<!DOCTYPE html>
<html lang="en">
<head>
<meta charset="utf-8">
<title>Brelvan Industries – Business Card</title>
<link rel="stylesheet" href="https://fonts.googleapis.com/css2?family=Tinos:wght@400;700&display=swap">
<style>
  :root {
    --brand-blue: #132b8f;
    --brand-red: #e00a0a;
    --shadow-tint: #dde1f3;
    --paper: #ffffff;
    --text-light: #ffffff;
  }
  html, body {
    margin: 0;
    padding: 0;
    overflow: hidden;
    background: var(--paper);
  }
  .card {
    position: relative;
    width: 1200px;
    height: 684px;
    overflow: hidden;
    background: var(--paper);
    font-family: "Tinos", "Times New Roman", serif;
  }
  .card__shapes {
    position: absolute;
    inset: 0;
  }
  .brand {
    position: absolute;
    left: 44px;
    top: 36px;
    display: inline-block;
    color: var(--brand-blue);
    font-weight: 700;
    line-height: 1;
    text-align: right;
  }
  .brand__name {
    display: block;
    font-size: 104px;
    letter-spacing: 1px;
    text-align: left;
  }
  .brand__sub {
    display: block;
    font-size: 34px;
    margin-top: 4px;
    padding-right: 14px;
  }
  .contact {
    position: absolute;
    left: 606px;
    top: 386px;
    margin: 0;
    padding: 0;
    list-style: none;
    color: var(--text-light);
    font-size: 30px;
    font-weight: 400;
  }
  .contact__item {
    display: flex;
    align-items: center;
    height: 41px;
  }
  .contact__icon {
    width: 22px;
    height: 22px;
    margin-right: 18px;
    flex: none;
  }
</style>
</head>
<body>
<div class="card">
  <svg class="card__shapes" width="1200" height="684" viewBox="0 0 1200 684" aria-hidden="true">
    <rect class="rule rule--top-long" x="0" y="220" width="672" height="9" fill="var(--brand-red)"/>
    <rect class="rule rule--top-short" x="0" y="243" width="413" height="9" fill="var(--brand-red)"/>
    <polygon class="wedge-shadow" points="346,428 676,684 716,684 362,414" fill="var(--shadow-tint)"/>
    <polygon class="wedge" points="346,400 1200,0 1200,684 708,684" fill="var(--brand-blue)"/>
    <rect class="rule rule--bottom-short" x="786" y="619" width="414" height="7" fill="var(--brand-red)"/>
    <rect class="rule rule--bottom-long" x="526" y="642" width="674" height="8" fill="var(--brand-red)"/>
  </svg>

  <div class="brand">
    <span class="brand__name">BRELVAN</span>
    <span class="brand__sub">Industries</span>
  </div>

  <ul class="contact">
    <li class="contact__item">
      <svg class="contact__icon" viewBox="0 0 22 22" fill="none" stroke="currentColor" stroke-width="1.4"><rect x="6" y="1" width="10" height="20" rx="2"/><line x1="9.5" y1="18" x2="12.5" y2="18"/></svg>
      (360) 555-0174
    </li>
    <li class="contact__item">
      <svg class="contact__icon" viewBox="0 0 22 22" fill="none" stroke="currentColor" stroke-width="1.4"><path d="M11 21s-7-7.2-7-12a7 7 0 0 1 14 0c0 4.8-7 12-7 12z"/><circle cx="11" cy="9" r="2.6"/></svg>
      61807 19th Street N, Marlow, OR 98517
    </li>
    <li class="contact__item">
      <svg class="contact__icon" viewBox="0 0 22 22" fill="none" stroke="currentColor" stroke-width="1.3"><circle cx="11" cy="11" r="9"/><ellipse cx="11" cy="11" rx="4" ry="9"/><line x1="2" y1="11" x2="20" y2="11"/><line x1="3.5" y1="6.5" x2="18.5" y2="6.5"/><line x1="3.5" y1="15.5" x2="18.5" y2="15.5"/></svg>
      marcus@kestrelbayholding.com
    </li>
    <li class="contact__item">
      <svg class="contact__icon" viewBox="0 0 22 22" fill="none" stroke="currentColor" stroke-width="1.4"><rect x="2" y="5" width="18" height="12"/><polyline points="2,5 11,12 20,5"/><line x1="2" y1="17" x2="8.5" y2="10.5"/><line x1="20" y1="17" x2="13.5" y2="10.5"/></svg>
      brelvanindustries.com
    </li>
  </ul>
</div>
</body>
</html>
```